The most modern business card ever !!!

Our company call “Vantilo”. Vantilo is a technology company specialized in cruises solutions. Out main product is a platform to reserve cruises. This is a revolutionary platform that make easier to travel agencies and final users to reserve cruises across dozen companies like tarvik, welbi, dpv, hbt, etc..We are a “start up”, with a young team of developers and we want to transmit it.. For it, we want something different, a modern business card that represent cruises and technology.. When someone receive this card, this person should say: wowww this is different… this is modern… this is a cruise related company..
Contact Information for Business Card
Requirements
Must have
- diferent, modern
Should not have
- traditions business card

```html
<!DOCTYPE html>
<html lang="en">
<head>
<meta charset="utf-8">
<title>Vantilo Business Card</title>
<link href="https://fonts.googleapis.com/css2?family=Quicksand:wght@500;600;700&family=Open+Sans:wght@600&display=swap" rel="stylesheet">
<style>
  :root {
    --bg: #e6ecef;
    --brand-blue: #2eaae2;
    --brand-blue-deep: #1f8fc2;
    --ink: #161616;
    --paper: #ffffff;
    --paper-cut: #eef2f4;
    --muted: #2b2b2b;
    --shadow: rgba(20, 40, 50, 0.18);
  }
  * { box-sizing: border-box; margin: 0; padding: 0; }
  html, body {
    width: 1200px; height: 960px; overflow: hidden;
    background: var(--bg);
  }
  .sheet { position: relative; width: 1200px; height: 960px; }
  .card {
    position: absolute; left: 260px;
    width: 680px; height: 388px;
    border-radius: 22px;
    box-shadow: 0 10px 30px var(--shadow);
    overflow: hidden;
  }
  .card--front { top: 70px; background: var(--brand-blue); }
  .card--back { top: 502px; background: var(--paper); }

  /* die-cut mark area: plain recessed square */
  .diecut {
    position: absolute; width: 104px; height: 104px;
    border-radius: 4px;
  }
  .card--front .diecut {
    left: 64px; top: 52px;
    background: var(--brand-blue-deep);
    box-shadow: inset 6px 6px 10px rgba(0, 0, 0, 0.28), inset -2px -2px 4px rgba(255, 255, 255, 0.25);
  }
  .card--back .diecut {
    right: 72px; top: 40px;
    background: var(--paper-cut);
    box-shadow: inset 6px 6px 10px rgba(0, 0, 0, 0.22), inset -2px -2px 4px rgba(255, 255, 255, 0.9);
  }

  .wordmark {
    position: absolute;
    font-family: "Quicksand", sans-serif;
    font-weight: 700;
    color: var(--ink);
    line-height: 1;
  }
  .card--front .wordmark { right: 40px; bottom: 46px; font-size: 86px; letter-spacing: 3px; }
  .card--back .wordmark { left: 50px; top: 36px; font-size: 54px; letter-spacing: 7px; }

  .holder {
    position: absolute; left: 62px; top: 184px;
    font-family: "Quicksand", sans-serif;
  }
  .holder__name { font-size: 34px; font-weight: 500; color: var(--muted); letter-spacing: 2px; }
  .holder__title { font-size: 15px; font-weight: 500; color: var(--brand-blue); margin-top: 2px; }

  .contacts {
    position: absolute; left: 56px; right: 36px; top: 282px;
    display: flex; align-items: center; gap: 32px;
    font-family: "Open Sans", sans-serif; font-weight: 600;
    font-size: 16px; color: var(--ink);
  }
  .contact { display: flex; align-items: center; gap: 9px; white-space: nowrap; }
  .contact svg { width: 16px; height: 14px; fill: var(--brand-blue); flex: none; }
  .contact--web svg { fill: none; stroke: var(--brand-blue); stroke-width: 1.4; }
</style>
</head>
<body>
<main class="sheet">
  <section class="card card--front" aria-label="Card front">
    <div class="diecut" role="img" aria-label="Die-cut brand mark area"></div>
    <div class="wordmark">Vantilo</div>
  </section>

  <section class="card card--back" aria-label="Card back">
    <div class="wordmark">Vantilo</div>
    <div class="diecut" role="img" aria-label="Die-cut brand mark area"></div>
    <div class="holder">
      <p class="holder__name">Your Name</p>
      <p class="holder__title">Job Title</p>
    </div>
    <div class="contacts">
      <span class="contact contact--phone">
        <svg viewBox="0 0 16 14" aria-hidden="true"><path d="M1 3c2-2.5 12-2.5 14 0v2h-4V3.5H5V5H1z"/><rect x="3" y="6" width="10" height="7" rx="1.5"/></svg>
        000 000 0000
      </span>
      <span class="contact contact--mail">
        <svg viewBox="0 0 16 14" aria-hidden="true"><rect x="1" y="2" width="14" height="10" rx="1.5"/></svg>
        youremail@xyz.com
      </span>
      <span class="contact contact--web">
        <svg viewBox="0 0 16 14" aria-hidden="true"><circle cx="8" cy="7" r="6"/><ellipse cx="8" cy="7" rx="2.6" ry="6"/><path d="M2 7h12"/></svg>
        www.yourwebsite.com
      </span>
    </div>
  </section>
</main>
</body>
</html>
```